Legal startup needs minimalistic websitebanner/header design

Hello Creatives!

I would like to update the banner/header on my website (https://lnk.example/7QwZpRe) to align with the overall style/feeling of the website. With banner/header I mean the image/illustration below the menu items, and above the page content (see attached screenshot for explanation).

Please don't let me limit your creatvity, but in general I like the following:
- Calm colors (preferably blue), combined with greyscale.
- Minimalistic/abstract design
- Simple and beautiful
- Communicates trust, quality

Requirements:
- Dimensions: 1331/389 px
- File format that is optimal for online presentation.
- Banners should look sharp (enough PPI?)

This contest is for 1 banner only. If you win, I would like to hire you to create banners for the other pages on my website as well (based on the winning banner design - with only small changes to make each webpage unique).

Looking forward to see your submissions!

Kind regards,
Maarten

Target Market(s)

Large corporations

Industry/Entity Type

Legal

Colors
0054AA
0677BA
7BADD7
CADEEF
E8F1F8

Requirements
Should not have
• Images of people, letters, many colors, busy patterns.

```html
<!DOCTYPE html>
<html lang="en">
<head>
<meta charset="utf-8">
<title>Harbourline Privacy – Header</title>
<link href="https://fonts.googleapis.com/css2?family=Source+Sans+3:wght@400;600&family=Work+Sans:wght@400;500&display=swap" rel="stylesheet">
<style>
  :root{
    --page-bg:#e6e6e6;
    --white:#ffffff;
    --navy:#0a2a7c;
    --brand:#0054aa;
    --action:#0a7cf4;
    --nav-text:#3a3a3a;
    --sky-1:#e8f1f8;
    --sky-2:#cadeef;
    --hex-light:#9fd4fb;
    --hex-mid:#7fc4fa;
    --hex-deep:#6aa6f3;
  }
  *{box-sizing:border-box;margin:0;padding:0}
  html,body{width:1200px;height:755px;overflow:hidden;background:var(--page-bg)}
  .site{
    position:absolute;left:203px;top:111px;width:806px;height:446px;
    background:var(--white);overflow:hidden;
  }
  .site-header{
    position:relative;height:55px;display:flex;align-items:center;
    padding:0 20px 0 19px;justify-content:space-between;
  }
  .brand{display:flex;align-items:center;gap:6px;
    font-family:"Source Sans 3",sans-serif;font-weight:600;font-size:17px;color:var(--brand);letter-spacing:.2px}
  .brand-mark{width:12px;height:12px;background:var(--brand)}
  .main-nav{display:flex;align-items:center;gap:18px;
    font-family:"Work Sans",sans-serif;font-size:9px;font-weight:500;letter-spacing:.6px;color:var(--nav-text)}
  .main-nav .nav-contact{background:var(--action);color:var(--white);padding:6px 16px;margin-left:-9px;width:80px;text-align:center}
  .hero{
    position:relative;height:391px;
    background:linear-gradient(90deg,var(--white) 0%,var(--sky-1) 40%,var(--sky-2) 100%);
  }
  .hex-cluster{position:absolute}
  .hex-cluster--top{
    left:555px;top:0;width:251px;height:156px;
    background:linear-gradient(135deg,var(--hex-light),var(--hex-mid) 55%,var(--hex-deep));
    clip-path:polygon(18% 30%,30% 0,100% 0,100% 100%,84% 90%,53% 80%,2% 72%,0 55%);
  }
  .hex-cluster--bottom{
    left:0;top:233px;width:283px;height:158px;
    background:linear-gradient(315deg,var(--hex-light),var(--hex-mid) 45%,var(--hex-deep));
    clip-path:polygon(0 4%,20% 10%,53% 27%,76% 32%,97% 38%,100% 53%,95% 78%,72% 100%,0 100%);
  }
  .hero-title{
    position:absolute;left:0;right:0;top:127px;text-align:center;
    font-family:"Source Sans 3",sans-serif;font-weight:400;font-size:23.5px;line-height:29px;color:var(--navy);
  }
  .values{position:absolute;top:201px;left:0;right:0;height:80px}
  .value{position:absolute;width:140px;margin-left:-70px;text-align:center;
    font-family:"Source Sans 3",sans-serif;font-size:13.5px;color:var(--navy)}
  .value svg{display:block;margin:0 auto 6px;height:43px}
  .value--trust{left:203px}
  .value--focus{left:405px}
  .value--pro{left:568px}
</style>
</head>
<body>
<div class="site">
  <header class="site-header">
    <div class="brand"><span class="brand-mark"></span>Harbourline Privacy</div>
    <nav class="main-nav">
      <span>ABOUT US</span><span>SERVICES</span><span>PRIVACY TOOLBOX</span><span>ARTICLES</span>
      <span class="nav-contact">CONTACT</span>
    </nav>
  </header>
  <section class="hero">
    <div class="hex-cluster hex-cluster--top" role="img" aria-label="Cluster of light blue 3D hexagon tiles"></div>
    <div class="hex-cluster hex-cluster--bottom" role="img" aria-label="Cluster of light blue 3D hexagon tiles"></div>
    <h1 class="hero-title">No-nonsense privacy guidance that adds value to your<br>organisation</h1>
    <div class="values">
      <div class="value value--trust">
        <svg viewBox="0 0 70 43" width="70" fill="var(--brand)">
          <rect x="1" y="3" width="9" height="16" rx="1" transform="rotate(30 5 11)"/>
          <rect x="60" y="3" width="9" height="16" rx="1" transform="rotate(-30 65 11)"/>
          <path d="M12 10 L28 8 L36 14 L44 8 L58 10 L54 24 L40 38 Q36 42 32 38 L16 26 Z"/>
          <path d="M30 14 L36 20 L42 14" stroke="var(--sky-1)" stroke-width="2" fill="none"/>
        </svg>
        TRUST
      </div>
      <div class="value value--focus">
        <svg viewBox="0 0 44 43" width="44" fill="var(--brand)">
          <rect x="0" y="0" width="2" height="43"/><rect x="0" y="41" width="44" height="2"/>
          <rect x="7" y="26" width="5" height="11" rx="2"/><rect x="15" y="22" width="5" height="15" rx="2"/>
          <rect x="23" y="18" width="5" height="19" rx="2"/><rect x="31" y="13" width="5" height="24" rx="2"/>
          <path d="M6 20 L34 6" stroke="var(--brand)" stroke-width="2"/><path d="M30 3 L40 3 L36 12 Z"/>
        </svg>
        BUSINESS FOCUS
      </div>
      <div class="value value--pro">
        <svg viewBox="0 0 46 43" width="46" fill="var(--brand)">
          <path d="M16 6 V1 H30 V6 H27 V4 H19 V6 Z"/>
          <rect x="0" y="7" width="46" height="13" rx="1"/>
          <rect x="1" y="21" width="44" height="22" rx="1"/>
          <rect x="20" y="19" width="6" height="5" fill="var(--sky-1)"/>
        </svg>
        PROFESSIONAL
      </div>
    </div>
  </section>
</div>
</body>
</html>
```